"Warm Granny" Snow & Ice Melt Package Design

Our company, Corvel Seasonal Products manufactures ice melt for melting snow. We are in the process of developing a new bag design for an ice melt product called "Warm Granny". It's a play on words obviously. The "Hot" is to reflect the power of the ice melt, :-). The bag dimentions are 14" x 26".
To get an idea of our current product packaging go to our website at http://www.corvelsp.example
Thank you and good luck.

Reason: Need more time for a few design updates. Thanks, Lionel

Reason: Need one more day

```html
<!DOCTYPE html>
<html lang="en">
<head>
<meta charset="utf-8">
<title>Fiery Nellie Snow &amp; Ice Melt</title>
<link rel="stylesheet" href="https://fonts.googleapis.com/css2?family=Fredoka:wght@600;700&family=PT+Sans:wght@400&display=swap">
<style>
  :root {
    --canvas: #f1f1f1;
    --paper: #ffffff;
    --panel: #231f20;
    --silhouette: #3b3a3b;
    --red: #ed1c24;
    --blue: #29a8e0;
    --stripe-blue: #1c75bc;
    --ink: #3a3a3a;
    --white: #ffffff;
  }
  * { margin: 0; padding: 0; box-sizing: border-box; }
  html, body { width: 986px; height: 1200px; overflow: hidden; background: var(--canvas); }
  .canvas { position: relative; width: 986px; height: 1200px; }
  .bag-face {
    position: absolute; left: 222px; top: 100px; width: 541px; height: 1000px;
    background: var(--paper);
  }
  .hero-panel {
    position: absolute; left: 0; top: 0; width: 541px; height: 670px;
    background: var(--panel); overflow: hidden;
  }
  .legs-art {
    position: absolute; left: 0; top: 0; width: 541px; height: 670px;
    background: radial-gradient(ellipse 34% 70% at 40% 45%, var(--silhouette) 0%, var(--panel) 100%);
  }
  .product-name {
    position: absolute; left: 0; top: 30px; width: 541px; text-align: center;
    font-family: "Fredoka", sans-serif; font-weight: 700; line-height: 1;
  }
  .product-name .line-one { display: block; color: var(--red); font-size: 150px; letter-spacing: -2px; }
  .product-name .line-two { display: block; color: var(--blue); font-size: 120px; margin-top: 20px; }
  .product-type {
    position: absolute; right: 30px; top: 614px; line-height: 1;
    font-family: "Fredoka", sans-serif; font-weight: 700; font-size: 38px;
    color: var(--white); letter-spacing: 0.5px;
  }
  .stripe-red { position: absolute; left: 0; top: 670px; width: 541px; height: 10px; background: var(--red); }
  .stripe-blue { position: absolute; left: 0; top: 680px; width: 541px; height: 20px; background: var(--stripe-blue); }
  .info-text {
    font-family: "PT Sans", sans-serif; font-size: 7.4px; line-height: 8.9px; color: var(--ink);
  }
  .info-columns {
    position: absolute; left: 42px; top: 713px; width: 456px;
    display: flex; gap: 9px;
  }
  .info-columns .info-text { width: 146px; }
  .divider { position: absolute; left: 40px; top: 854px; width: 458px; height: 11px; background: var(--stripe-blue); }
  .info-wide { position: absolute; left: 43px; top: 877px; width: 450px; }
  .brand-mark {
    position: absolute; left: 63px; top: 940px; line-height: 1;
    font-family: "Fredoka", sans-serif; font-weight: 700; font-size: 24px; color: var(--red);
  }
  .info-tail { position: absolute; left: 231px; top: 938px; width: 258px; }
</style>
</head>
<body>
<div class="canvas">
  <div class="bag-face">
    <div class="hero-panel">
      <div class="legs-art" role="img" aria-label="Grey silhouette of a woman's legs in high-heeled boots, striding"></div>
      <h1 class="product-name">
        <span class="line-one">FIERY</span>
        <span class="line-two">Nellie</span>
      </h1>
      <p class="product-type">SNOW &amp; ICE MELT</p>
    </div>
    <div class="stripe-red"></div>
    <div class="stripe-blue"></div>

    <div class="info-columns">
      <p class="info-text">Home &gt; Ice Melters &gt; Glacivo<br>Calcium Chloride Pellets also known by the brand name Glacivo has been recognized by the industry as the most effective ice melter. Glacivo melts ice upon contact and is among the most powerful substances available today for melting snow and ice. Most de-icers become virtually ineffective once the temperature drops below +20 degrees while Glacivo keeps on melting even at temperatures as cold as 25 degrees below zero. Glacivo is also safer to use and does not chemically attack concrete.</p>
      <p class="info-text">Home &gt; Ice Melters &gt; Glacivo<br>Calcium Chloride Pellets also known by the brand name Glacivo has been recognized by the industry as the most effective ice melter. Glacivo melts ice upon contact and is among the most powerful substances available today for melting snow and ice. Most de-icers become virtually ineffective once the temperature drops below +20 degrees while Glacivo keeps on melting even at temperatures as cold as 25 degrees below zero. Glacivo is also safer to use and does not chemically attack concrete.</p>
      <p class="info-text">Home &gt; Ice Melters &gt; Glacivo<br>Calcium Chloride Pellets also known by the brand name Glacivo has been recognized by the industry as the most effective ice melter. Glacivo melts ice upon contact and is among the most powerful substances available today for melting snow and ice. Most de-icers become virtually ineffective once the temperature drops below +20 degrees while Glacivo keeps on melting even at temperatures as cold as 25 degrees below zero. Glacivo is also safer to use and does not chemically attack concrete.</p>
    </div>

    <div class="divider"></div>

    <p class="info-text info-wide">Home &gt; Ice Melters &gt; Glacivo<br>Calcium Chloride Pellets also known by the brand name Glacivo has been recognized by the industry as the most effective ice melter. Glacivo melts ice upon contact and is among the most powerful substances available today for melting snow and ice. Most de-icers become virtually ineffective once the temperature drops below +20 degrees while Glacivo keeps on melting even at temperatures as cold as 25 degrees below zero. Glacivo is also safer to use and does not chemically attack concrete.</p>

    <p class="brand-mark">Fiery Nellie</p>

    <p class="info-text info-tail">Home &gt; Ice Melters &gt; Glacivo<br>Calcium Chloride Pellets also known by the brand name Glacivo has been recognized by the industry as the most effective ice melter. Glacivo melts ice upon contact and is among the most powerful substances available today for melting</p>
  </div>
</div>
</body>
</html>
```